Life Insurance Landing Page (for lead gen)

We need a high converting life insurance page created. It will be housed at www.CoverageVerifyHub.com. We will be driving former life insurance prospects to this page where they will only need to confirm their phone number & email in order to receive an updated quote.
Updates

Only the page design is required, the coding will be done on our end. 

Target Market(s)

People who have expressed an interest in obtaining life insurance.

Industry/Entity Type

Life Insurance

Requirements
Must have
• 1) Under "CoverageVerifyHub.com" Please include a "Powered by KRBT" tag and match the colors of this site: http://thekrbt.com/life-insurance-services.html to the page.

2) The form should ask for their phone number and include an appointment calendar widget (we'll code the functionality) so they can choose the date/time of their call. It should also have an email confirmation field.

3) the overall message next to the form fields should be "Thanks for visiting Gordon (we'll personalize this "firstname" field ), please let us know the best time to schedule a brief call so we can give you an updated, rock bottom pricing quote on a policy. We'll also email you with the information, please confirm your email here and we'll send you the details.

4) We'd like to include a box that appears to be a personalized "quote briefing" snapshot that will list this information: "Name: _________" "Birth Date:"____________" "Policy Type: _______", "Coverage Amount: ____________" " all these fields will be populated into the page.

```html
<!DOCTYPE html>
<html lang="en">
<head>
<meta charset="utf-8">
<title>CoverageVerifyHub.com – Life Insurance Quote</title>
<link rel="stylesheet" href="https://fonts.googleapis.com/css2?family=Open+Sans:wght@400;600;700&display=swap">
<style>
  :root{
    --blue:#2480c3;
    --blue-dark:#1a5f96;
    --ink:#4a4f55;
    --muted:#7b838b;
    --line:#d6dde3;
    --page:#e9eef2;
    --panel:#ffffff;
    --hero-top:#f4f7fa;
    --hero-bottom:#dfe8ef;
    --accent:#f0a01f;
    --soft:#f3f7fa;
  }
  *{box-sizing:border-box;margin:0;padding:0}
  html,body{width:667px;height:1200px;overflow:hidden}
  body{background:var(--page);font-family:"Open Sans",Arial,sans-serif;color:var(--ink);font-size:6.6px;line-height:1.65}

  .site-header{height:44px;background:var(--blue);color:#fff}
  .site-header .wrap{width:560px;margin:0 auto;position:relative;height:44px}
  .brand{position:absolute;left:0;top:6px}
  .brand-name{font-size:15px;font-weight:700;line-height:1.2}
  .brand-tag{font-size:6.5px;font-weight:600;opacity:.9}
  .social{position:absolute;right:0;top:15px;display:flex;gap:5px}
  .social span{width:11px;height:11px;border-radius:50%;background:#fff;opacity:.85}

  .hero{height:282px;background:linear-gradient(var(--hero-top),var(--hero-bottom))}
  .hero .wrap{width:560px;margin:0 auto;position:relative;height:282px}
  .hero h1{position:absolute;left:0;top:16px;font-size:21px;font-weight:600;color:var(--blue);letter-spacing:-.2px;line-height:1.3}
  .hero-copy{position:absolute;left:0;top:50px;width:200px;font-size:7px;line-height:1.5}
  .hero-form{position:absolute;left:0;top:100px;width:150px}
  .field{height:14px;background:#fff;border:1px solid var(--line);margin-bottom:5px;font-size:6.2px;color:#9aa2a9;padding:1px 5px;line-height:11px}
  .date-row{display:flex;gap:3px;align-items:center;font-size:6px}
  .date-row .sel{height:12px;border:1px solid var(--line);background:#fff;flex:1;font-size:5.5px;padding:0 3px;line-height:10px;color:var(--muted)}
  .date-row .go{height:12px;width:16px;background:var(--blue)}
  .calendar{position:absolute;left:55px;top:180px;width:136px;background:#fff;border:1px solid var(--line);box-shadow:0 2px 4px rgba(0,0,0,.15);padding:4px;z-index:2;line-height:1.4}
  .cal-head{display:flex;justify-content:space-between;font-size:6.5px;font-weight:700;margin-bottom:2px}
  .calendar table{width:100%;border-collapse:collapse;font-size:5.6px;text-align:center}
  .calendar th{color:var(--muted);font-weight:600;padding:1px 0}
  .calendar td{padding:1.5px 0;border:1px solid #eef1f4}
  .calendar td.on{background:var(--blue);color:#fff}
  .calendar td.off{color:#c3c9ce}
  .cal-foot{display:flex;justify-content:space-between;margin-top:3px;font-size:5.5px}
  .cal-foot span{background:#eef1f4;padding:1px 4px}
  .hero-photo{position:absolute;right:-26px;top:0;width:330px;height:282px;background:linear-gradient(160deg,#e6d8cc 0%,#cfc4bd 40%,#c3d2de 75%,#dbe5ec 100%)}

  .content{width:560px;margin:0 auto;background:var(--panel);display:flex;height:794px}
  .main{width:395px;padding:10px 12px 0 12px}
  .aside{width:165px;padding:10px 10px 0 4px}

  .intro{display:flex;gap:9px;min-height:92px}
  .briefing{width:112px;flex:none;border:1px solid var(--line);background:var(--soft);padding:5px 6px}
  .briefing h4{font-size:7.4px;color:var(--blue);font-weight:700;margin-bottom:3px}
  .brief-row{display:flex;justify-content:space-between;border-bottom:1px dotted var(--line);font-size:6px;line-height:1.9}
  .brief-row b{font-weight:600}
  .intro-text{flex:1}
  h2{font-size:10px;color:var(--blue);font-weight:600;margin-bottom:3px;line-height:1.3}
  h3{font-size:8.5px;color:var(--blue);font-weight:600;margin:9px 0 3px;line-height:1.3}
  p{margin-bottom:5px}
  .rule{border-top:1px solid var(--line);margin:6px 0 8px}

  .offer{border-left:1px solid var(--line);padding-left:10px;min-height:92px}
  .offer ul{list-style:none}
  .offer li{display:flex;align-items:center;gap:4px;line-height:1.75}
  .offer li svg{width:6px;height:6px}

  .changes ul{list-style:none;margin:3px 0 6px}
  .changes li{position:relative;padding-left:8px;line-height:1.75}
  .changes li::before{content:"";position:absolute;left:1px;top:4px;width:3px;height:3px;background:var(--blue);border-radius:50%}

  .box{border:1px solid var(--line);margin-bottom:12px}
  .box-head{background:var(--blue);color:#fff;font-size:10px;font-weight:700;padding:5px 7px;line-height:1.3}
  .box-body{padding:8px 7px}
  .box .field{height:16px;margin-bottom:7px;line-height:13px}
  .btn{background:var(--blue-dark);color:#fff;font-size:6.5px;font-weight:600;padding:3px 8px;line-height:1.4}
  .btn.center{display:block;width:56px;margin:2px auto 0;text-align:center}

  .need{background:var(--blue);color:#fff;margin-bottom:12px;padding:8px 8px 10px}
  .need h4{font-size:11px;font-weight:700;margin-bottom:2px;line-height:1.3}
  .need p{font-size:7px;line-height:1.45}
  .need-photo{height:130px;margin:6px -8px 8px;background:linear-gradient(#6aa8d6,#3c82b8)}
  .need .btn{background:var(--accent);padding:5px 6px}

  .site-footer{margin-top:6px}
  .site-footer .wrap{width:560px;margin:0 auto;background:#d5dfe7;padding:7px 0;text-align:center;color:var(--muted);font-size:5.5px;line-height:1.6}
</style>
</head>
<body>

<header class="site-header">
  <div class="wrap">
    <div class="brand">
      <div class="brand-name">www.CoverageVerifyHub.com</div>
      <div class="brand-tag">Powered by KRBT</div>
    </div>
    <div class="social"><span></span><span></span><span></span></div>
  </div>
</header>

<section class="hero">
  <div class="wrap">
    <div class="hero-photo" role="img" aria-label="Photo of a smiling senior couple embracing outdoors"></div>
    <h1>Thanks for visiting Gordon</h1>
    <p class="hero-copy">Please let us know the best time to schedule a brief call so we can give you an updated, rock bottom pricing quote on a policy. We'll also email you with the information, please confirm your email here and we'll send you the details.</p>
    <div class="hero-form">
      <div class="field">Name*</div>
      <div class="field">Email*</div>
      <div class="field">Phone*</div>
      <div class="date-row">Date <span class="sel">mm/dd/yyyy</span><span class="sel">Time</span><span class="go"></span></div>
    </div>
    <div class="calendar">
      <div class="cal-head"><span>‹</span><span>April 2016</span><span>›</span></div>
      <table>
        <tr><th>Su</th><th>Mo</th><th>Tu</th><th>We</th><th>Th</th><th>Fr</th><th>Sa</th></tr>
        <tr><td class="off">27</td><td class="off">28</td><td class="off">29</td><td class="off">30</td><td class="off">31</td><td>1</td><td>2</td></tr>
        <tr><td>3</td><td>4</td><td>5</td><td>6</td><td>7</td><td class="on">8</td><td>9</td></tr>
        <tr><td>10</td><td>11</td><td>12</td><td>13</td><td>14</td><td>15</td><td>16</td></tr>
        <tr><td>17</td><td>18</td><td>19</td><td>20</td><td>21</td><td>22</td><td>23</td></tr>
        <tr><td>24</td><td>25</td><td>26</td><td>27</td><td>28</td><td>29</td><td>30</td></tr>
      </table>
      <div class="cal-foot"><span>Today</span><span>Done</span></div>
    </div>
  </div>
</section>

<div class="content">
  <div class="main">
    <div class="intro">
      <div class="briefing">
        <h4>Your Quote Briefing</h4>
        <div class="brief-row"><b>Name:</b><span>Gordon</span></div>
        <div class="brief-row"><b>Birth Date:</b><span>__________</span></div>
        <div class="brief-row"><b>Policy Type:</b><span>__________</span></div>
        <div class="brief-row"><b>Coverage Amount:</b><span>________</span></div>
      </div>
      <div class="intro-text">
        <h2>Life Insurance</h2>
        <p>Life insurance is one of the most important purchases you will ever make. It gives the people who depend on you a way to keep their home, pay daily costs and plan ahead if the unexpected happens.</p>
        <p>Talk to one of our agents about the cover that fits your family, budget and goals. We compare many carriers so you get a fair price fast.</p>
      </div>
    </div>
    <div class="rule"></div>
    <div class="changes">
      <h2>Life changes - so should your policy</h2>
      <p>Each year, many people buy a policy and then never look at it again. Your needs change over time, and your cover should keep pace. It may be time to review your policy if:</p>
      <ul>
        <li>You recently married or divorced</li>
        <li>You have a new child or grandchild</li>
        <li>You have started or expanded a business</li>
        <li>Your health or your spouse's health has changed</li>
        <li>You are providing care or financial assistance to a parent</li>
        <li>Your child or grandchild requires assistance or long-term care</li>
        <li>You recently purchased a new home</li>
        <li>You are planning for a child or grandchild's education</li>
        <li>You are concerned about retirement income</li>
        <li>You have refinanced your home mortgage in the past six months</li>
        <li>You or your spouse recently received an inheritance</li>
        <li>You have a sizable estate</li>
      </ul>
    </div>
    <div class="rule"></div>
    <h2>California - why you need to know about life insurance</h2>
    <p>Living costs in the state are among the highest in the nation, so the income your family relies on matters more than ever. A policy helps protect that income, pay off debt and keep long term plans on track. Below are the main types of cover to consider.</p>
    <h3>Term Life Insurance</h3>
    <p>Term life insurance provides protection for a set period of time, such as ten, twenty or thirty years. If you pass away during the term, your beneficiaries receive the death benefit. It is often the most affordable way to buy a large amount of cover, and many policies can be converted later on.</p>
    <h3>Whole Life Insurance</h3>
    <p>Whole life insurance stays in force for your entire life as long as premiums are paid. Premiums are fixed and the policy builds cash value over time that you can borrow against. It costs more than term cover, but it offers lasting protection and steady growth.</p>
    <p>Many families use whole life cover to leave a legacy, pay estate costs or give a child a head start.</p>
    <h3>Universal Life Insurance</h3>
    <p>Universal life insurance is a flexible form of permanent cover. You can adjust premiums and the death benefit as your needs change, within set limits. Cash value earns interest, which can help pay future premiums or support your long term plans.</p>
    <p>It suits people who want lifelong protection with room to adapt when income or family plans shift.</p>
    <h3>What are the advantages of life insurance?</h3>
    <p>Having the right life insurance is essential to planning for your family's future. The death benefit is generally paid free of income tax and can replace lost income, cover a mortgage, fund college or pay final expenses. It gives loved ones time to adjust without money worries.</p>
    <p>Some policies also build cash value you can use later in life, and many offer riders for illness, disability or long-term care. An agent can help you match features to your needs and keep costs low.</p>
    <p>Cover can also protect a business, fund a buy-sell agreement or keep a key partner's share in the right hands. For parents, it can pay for childcare and schooling so plans stay on course.</p>
    <p>The best time to buy is while you are young and healthy, since rates rise with age. Request your updated quote today and see how much you could save with a policy built around you.</p>
  </div>

  <aside class="aside">
    <div class="offer">
      <h2>What We Offer</h2>
      <ul>
        <li><svg viewBox="0 0 6 6"><path d="M.5 3l1.8 1.8L5.5 1" fill="none" stroke="#2480c3" stroke-width="1.2"/></svg>Auto Insurance</li>
        <li><svg viewBox="0 0 6 6"><path d="M.5 3l1.8 1.8L5.5 1" fill="none" stroke="#2480c3" stroke-width="1.2"/></svg>Home Insurance</li>
        <li><svg viewBox="0 0 6 6"><path d="M.5 3l1.8 1.8L5.5 1" fill="none" stroke="#2480c3" stroke-width="1.2"/></svg>Life Insurance</li>
        <li><svg viewBox="0 0 6 6"><path d="M.5 3l1.8 1.8L5.5 1" fill="none" stroke="#2480c3" stroke-width="1.2"/></svg>Health Insurance</li>
        <li><svg viewBox="0 0 6 6"><path d="M.5 3l1.8 1.8L5.5 1" fill="none" stroke="#2480c3" stroke-width="1.2"/></svg>Business Insurance</li>
        <li><svg viewBox="0 0 6 6"><path d="M.5 3l1.8 1.8L5.5 1" fill="none" stroke="#2480c3" stroke-width="1.2"/></svg>Restaurant Insurance</li>
        <li><svg viewBox="0 0 6 6"><path d="M.5 3l1.8 1.8L5.5 1" fill="none" stroke="#2480c3" stroke-width="1.2"/></svg>Workers Comp</li>
      </ul>
    </div>
    <div class="rule"></div>
    <div class="box">
      <div class="box-head">Get A Free Quote</div>
      <div class="box-body">
        <div class="field">Name</div>
        <div class="field">Email</div>
        <div class="field">Phone</div>
        <div class="field">Coverage Amount</div>
        <div class="btn center">Submit</div>
      </div>
    </div>
    <div class="need">
      <h4>Need a Quote?</h4>
      <p>Our Agents are ready to find out your needs and get you quotes</p>
      <div class="need-photo" role="img" aria-label="Photo of a support agent wearing a headset"></div>
      <div class="btn center">Get a Quote</div>
    </div>
    <div class="box">
      <div class="box-head">Sign Up For Newsletter</div>
      <div class="box-body">
        <div class="field">Enter email address</div>
        <div class="btn center">Subscribe</div>
      </div>
    </div>
  </aside>
</div>

<footer class="site-footer">
  <div class="wrap">
    CoverageVerifyHub.com &middot; Powered by KRBT<br>
    Licensed agents serving families across the state<br>
    Copyright 2016 &middot; All rights reserved
  </div>
</footer>

</body>
</html>
```